Create a mock up design for our tv recycling website.

Please create a mock up design for our television recycling website. Attached is the proof for our logo as well as the layout we have planned.

The winner of the contest should:

1) create a mock up design of our main page. (only the main page is required, if you want to create multiple pages, that is up to you)
2) create a design that is in line with the image we have roughly created and attached here for layout.
3) create a modern, unique design that gives us us a professional appearance and conveys the message that we are a recycling company but is not over the top with recycling graphics making it look tacky.
4)Create a design that makes someone stop and say WOW that is awesome.

Thank you!
Gus

```html
<!DOCTYPE html>
<html lang="en">
<head>
<meta charset="utf-8">
<title>Relay Screens – Television Recycling</title>
<link rel="stylesheet" href="https://fonts.googleapis.com/css2?family=Arimo:wght@400;700&family=Tinos:wght@700&display=swap">
<style>
:root{
  --black:#000;
  --white:#fff;
  --green:#1fd41f;
  --green-light:#3cf03c;
  --green-dark:#0a7a0a;
  --nav-green:#3ab83a;
  --orange:#ffa800;
  --red:#d8191c;
  --band:#b5dc6a;
  --text:#1a1a1a;
  --map:#ebe4d6;
  --footer-text:#c8c8c8;
}
*{margin:0;padding:0;box-sizing:border-box}
html,body{width:720px;height:1200px;overflow:hidden;background:var(--white)}
body{position:relative;font-family:"Arimo",Arial,sans-serif;color:var(--text)}
.abs{position:absolute}

.site-header{left:0;top:0;width:720px;height:90px;background:var(--black)}
.brand{left:62px;top:28px;display:flex;align-items:center;gap:8px;color:var(--green-light);font-weight:700;font-size:20px}
.brand-dot{width:20px;height:20px;border-radius:50%;background:var(--green)}
.phone{right:70px;top:15px;color:var(--white);font-family:"Tinos",serif;font-size:10px}
.main-nav{right:70px;top:38px;display:flex;font-family:"Tinos",serif;font-size:10.5px;color:var(--white)}
.main-nav span{padding:0 19px;border-left:1px solid var(--white);line-height:12px}
.main-nav span:first-child{border-left:none;color:var(--nav-green)}
.main-nav span:last-child{padding-right:0}

.hero{left:0;top:90px;width:720px;height:246px;background:linear-gradient(180deg,#17c417 0%,var(--green-light) 40%,#22dd22 70%,#109a10 100%)}
.hero-arrow{top:104px;width:40px;height:40px;border-radius:50%;background:rgba(255,255,255,.25);color:var(--white);font-size:26px;font-weight:700;text-align:center;line-height:38px}
.hero-arrow.prev{left:54px}
.hero-arrow.next{left:626px}
.hero-title{left:315px;top:60px;color:var(--white);font-size:22px;font-weight:400;letter-spacing:.3px}
.hero-sub{left:358px;top:102px;font-size:14px;line-height:21.5px;color:#111;letter-spacing:.3px}
.hero-sub em{font-style:normal;color:var(--red)}

.feature{top:354px;width:185px;height:174px;background:var(--orange);border-radius:0 0 4px 4px;padding:13px 11px;font-size:14.5px;line-height:21px;color:#222}
.feature .icon{position:absolute;left:54px;top:66px;width:78px;height:78px;border-radius:50%}
.f1{left:72px}.f2{left:268px}.f3{left:465px}
.f1 .icon{background:radial-gradient(circle,#8ee86a,#2f9e1f)}
.f2 .icon{background:radial-gradient(circle,#7fd84f,#3a8f1e);width:60px;left:62px;border-radius:30px}
.f3 .icon{background:radial-gradient(circle,#e3f7c2,#8fd64a)}

.section-title{left:0;width:720px;text-align:center;font-weight:700;font-size:29px;color:var(--black)}
.band{height:5px;background:repeating-linear-gradient(90deg,var(--band) 0 2px,#d9efb0 2px 3px)}

.about-text{left:59px;top:584px;width:594px;font-size:7px;line-height:11px}
.about-text p+p{margin-top:10px}
.logo-panel{left:59px;top:632px;width:251px;height:63px;background:linear-gradient(180deg,#fafafa,#cfcfcf);display:flex;align-items:center;justify-content:center;gap:10px;font-size:26px;font-weight:700;color:var(--green-dark)}
.logo-panel .brand-dot{width:28px;height:28px;background:var(--green-dark)}
.read-more{left:600px;top:638px;font-size:8px;font-weight:700;color:var(--green-dark)}

.map{left:0;top:720px;width:720px;height:264px;background:linear-gradient(160deg,#eee8dc,var(--map) 60%,#ddd6c6)}
.map-pin{left:364px;top:826px}
.location-label{left:250px;top:702px;width:204px;height:38px;background:var(--white);text-align:center;font-size:28px;font-weight:700;line-height:38px}

.why-text{left:59px;top:1033px;width:600px;font-size:7px;line-height:10.6px;font-weight:700;text-align:justify}

.site-footer{left:0;top:1110px;width:720px;height:90px;background:var(--black);color:var(--footer-text);font-size:8px;font-weight:700;text-align:center;line-height:11px}
.footer-col{position:absolute;top:16px}
.footer-col h4{font-size:8px;text-decoration:underline;margin-bottom:3px}
.links{left:88px;width:92px}
.share{left:312px;width:80px}
.share h4{font-family:"Tinos",serif}
.social{display:flex;justify-content:center;gap:8px;margin-top:4px}
.social span{width:33px;height:33px;border-radius:50%;background:#3d5e22;border:2px solid #222}
.contact{left:527px;width:140px}
</style>
</head>
<body>

<header class="site-header abs">
  <div class="brand abs"><span class="brand-dot"></span>Relay Screens</div>
  <div class="phone abs">555-201-3380</div>
  <nav class="main-nav abs"><span>Home</span><span>About Us</span><span>We Buy</span><span>Contact Us</span></nav>
</header>

<section class="hero abs">
  <div class="hero-arrow prev abs">&lt;</div>
  <div class="hero-arrow next abs">&gt;</div>
  <h1 class="hero-title abs">WE BUY BROKEN TELEVISION</h1>
  <p class="hero-sub abs">AN <em>ENVIRONMENTALLY</em><br>&nbsp;&nbsp;&nbsp;&nbsp;&nbsp;&nbsp;<em>ECONOMICALLY</em> CONCIOUS<br>&nbsp;&nbsp;&nbsp;&nbsp;&nbsp;&nbsp;&nbsp;&nbsp;&nbsp;&nbsp;TV DISPOSAL OPTION</p>
</section>

<div class="feature f1 abs">What is your TV worth?<div class="icon" role="img" aria-label="Green recycling icon"></div></div>
<div class="feature f2 abs">What TV we buy and recycle?<div class="icon" role="img" aria-label="Green dollar icon"></div></div>
<div class="feature f3 abs">What TV we dont buy and recycle?<div class="icon" role="img" aria-label="Crossed-out buy badge icon"></div></div>

<div class="band abs" style="left:0;top:548px;width:265px"></div>
<div class="band abs" style="left:451px;top:548px;width:269px"></div>
<h2 class="section-title abs" style="top:534px">About Us</h2>

<div class="about-text abs">
  <p>Relay Screens Sales and Service LLC is North Florida's leading in Television recycling ! We are an innovative company doing something that everyone said that was not possible !We are the first one to make &nbsp;it our mission to recycle your broken television that is no longer worth repairing or outlived its life span.</p>
  <p>We are here to serve you 6 days a week paying cash for yout crash television!</p>
</div>
<div class="logo-panel abs"><span class="brand-dot"></span>Relay Screens</div>
<div class="read-more abs">Read More&gt;&gt;</div>

<div class="band abs" style="left:0;top:716px;width:250px"></div>
<div class="band abs" style="left:454px;top:716px;width:266px"></div>
<div class="map abs" role="img" aria-label="Street map showing the drop-off location"></div>
<svg class="map-pin abs" width="26" height="42" viewBox="0 0 26 42" aria-hidden="true"><path d="M13 41 L3 20 A12 12 0 1 1 23 20 Z" fill="#e03a2e" stroke="#8a1a12"/></svg>
<h2 class="location-label abs">Location</h2>

<div class="band abs" style="left:0;top:1003px;width:250px"></div>
<div class="band abs" style="left:455px;top:1003px;width:265px"></div>
<h2 class="section-title abs" style="top:989px">Why Recycle</h2>
<p class="why-text abs">Lorem Ipsum is simply dummy text of the printing and typesetting industry. Lorem Ipsum has been the industry's standard dummy text ever since the 1500s, when an unknown printer took a galley of type and scrambled it to make a type specimen book. It has survived not only five centuries, but also the leap into electronic typesetting, remaining essentially unchanged. It was popularised in the 1960s with the release of Tessara sheets containing Lorem Ipsum passages, and more recently with desktop publishing software like Quillform Layout including versions of Lorem Ipsum.</p>

<footer class="site-footer abs">
  <div class="footer-col links"><h4>Links</h4><p>Need a TV Repaired ?</p></div>
  <div class="footer-col share"><h4>Share us on</h4><div class="social"><span></span><span></span></div></div>
  <div class="footer-col contact"><h4>Conatct us</h4><p>48 Harbor Mill Rd Unit C<br>Cedar Bend, FL 30000<br>5552013381</p></div>
</footer>

</body>
</html>
```